Graphic Design Project

I need to create a graphic design, which needs to be editable for me in Powerpoint... I have attached it a draft of it, but I need to be able to change the text of it. I want it to look more professional
Updates

Target Market(s)

Business Executives

Industry/Entity Type

Graphic Design

Requirements
Must have
• Make it look professional; the colors can change; I just need to be able to edit the text in powerpoint or either word

```html
<!DOCTYPE html>
<html lang="en">
<head>
<meta charset="utf-8">
<title>Managing Change – IT Service Pyramid</title>
<link rel="stylesheet" href="https://fonts.googleapis.com/css2?family=Carlito:wght@400;700&display=swap">
<style>
  :root {
    --page: #ffffff;
    --teal-top: #93b7bb; --teal-front: #5f8f96; --teal-side: #436b71;
    --orange-top: #eaa862; --orange-front: #d9842c; --orange-side: #a9641d;
    --red-top: #ea7a5f; --red-front: #d4472b; --red-side: #a2321d;
    --brown-top: #a4968e; --brown-front: #7c6f67; --brown-side: #584d47;
    --green-top: #a0c39d; --green-front: #6b9c69; --green-side: #4b784a;
    --base-light: #f2f2f2; --base-dark: #cfcfcf; --base-edge: #bdbdbd;
    --headline: #c0141a;
    --label: #ffffff;
  }
  html, body { margin: 0; padding: 0; background: var(--page); overflow: hidden; }
  .canvas { width: 1200px; height: 901px; display: block; }
  .block-label {
    font-family: "Carlito", "Calibri", Arial, sans-serif;
    font-weight: 700; font-size: 20px; fill: var(--label);
    text-anchor: middle;
    filter: drop-shadow(1px 1px 1px rgba(0,0,0,.45));
  }
  .block-label--small { font-size: 17px; }
  .block-label--apex { font-size: 19px; }
  .headline {
    font-family: "Carlito", "Calibri", Arial, sans-serif;
    font-weight: 700; font-size: 38px; fill: var(--headline);
    text-anchor: middle; letter-spacing: .5px;
  }
  .teal .top { fill: var(--teal-top); } .teal .front { fill: var(--teal-front); } .teal .side { fill: var(--teal-side); }
  .orange .top { fill: var(--orange-top); } .orange .front { fill: var(--orange-front); } .orange .side { fill: var(--orange-side); }
  .red .top { fill: var(--red-top); } .red .front { fill: var(--red-front); } .red .side { fill: var(--red-side); }
  .brown .top { fill: var(--brown-top); } .brown .front { fill: var(--brown-front); } .brown .side { fill: var(--brown-side); }
  .green .top { fill: var(--green-top); } .green .front { fill: var(--green-front); } .green .side { fill: var(--green-side); }
  .face-edge { stroke: rgba(255,255,255,.25); stroke-width: 1; }
</style>
</head>
<body>
<svg class="canvas" viewBox="0 0 1080 811" xmlns="http://www.w3.org/2000/svg">
  <defs>
    <linearGradient id="base-fill" x1="0" y1="0" x2="0" y2="1">
      <stop offset="0" stop-color="var(--base-light)"/>
      <stop offset="1" stop-color="var(--base-dark)"/>
    </linearGradient>
    <linearGradient id="front-sheen" x1="0" y1="0" x2="0" y2="1">
      <stop offset="0" stop-color="#fff" stop-opacity=".12"/>
      <stop offset="1" stop-color="#000" stop-opacity=".08"/>
    </linearGradient>
  </defs>

  <!-- Foundation -->
  <g class="foundation">
    <polygon points="92,580 885,580 840,612 728,645 300,645 135,612" fill="url(#base-fill)" stroke="var(--base-edge)" stroke-width="1"/>
    <text class="headline" x="487" y="626">MANAGING CHANGE</text>
  </g>

  <!-- Row 1 -->
  <g class="block teal">
    <polygon class="top face-edge" points="108,470 140,440 300,440 268,470"/>
    <polygon class="side" points="268,470 300,440 300,547 268,577"/>
    <rect class="front" x="108" y="470" width="160" height="107"/>
    <rect x="108" y="470" width="160" height="107" fill="url(#front-sheen)"/>
    <text class="block-label" x="188" y="504">Customer</text>
    <text class="block-label" x="188" y="533">Engagement</text>
    <text class="block-label" x="188" y="562">Model</text>
  </g>
  <g class="block orange">
    <polygon class="top face-edge" points="306,470 338,440 498,440 466,470"/>
    <polygon class="side" points="466,470 498,440 498,547 466,577"/>
    <rect class="front" x="306" y="470" width="160" height="107"/>
    <rect x="306" y="470" width="160" height="107" fill="url(#front-sheen)"/>
    <text class="block-label" x="386" y="504">Service-</text>
    <text class="block-label" x="386" y="533">Minded</text>
    <text class="block-label" x="386" y="562">IT Culture</text>
  </g>
  <g class="block red">
    <polygon class="top face-edge" points="504,470 536,440 696,440 664,470"/>
    <polygon class="side" points="664,470 696,440 696,547 664,577"/>
    <rect class="front" x="504" y="470" width="160" height="107"/>
    <rect x="504" y="470" width="160" height="107" fill="url(#front-sheen)"/>
    <text class="block-label" x="584" y="504">Policy,</text>
    <text class="block-label" x="584" y="533">Process &amp;</text>
    <text class="block-label block-label--small" x="584" y="561">Methodologies</text>
  </g>
  <g class="block brown">
    <polygon class="top face-edge" points="705,470 737,440 897,440 865,470"/>
    <polygon class="side" points="865,470 897,440 897,547 865,577"/>
    <rect class="front" x="705" y="470" width="160" height="107"/>
    <rect x="705" y="470" width="160" height="107" fill="url(#front-sheen)"/>
    <text class="block-label" x="785" y="518">Meaningful</text>
    <text class="block-label" x="785" y="547">Metrics</text>
  </g>

  <!-- Row 2 -->
  <g class="block green">
    <polygon class="top face-edge" points="220,354 252,324 412,324 380,354"/>
    <polygon class="side" points="380,354 412,324 412,432 380,462"/>
    <rect class="front" x="220" y="354" width="160" height="108"/>
    <rect x="220" y="354" width="160" height="108" fill="url(#front-sheen)"/>
    <text class="block-label" x="300" y="403">Transform IT</text>
    <text class="block-label" x="300" y="432">Team</text>
  </g>
  <g class="block brown">
    <polygon class="top face-edge" points="430,354 462,324 622,324 590,354"/>
    <polygon class="side" points="590,354 622,324 622,432 590,462"/>
    <rect class="front" x="430" y="354" width="160" height="108"/>
    <rect x="430" y="354" width="160" height="108" fill="url(#front-sheen)"/>
    <text class="block-label" x="510" y="389">Master</text>
    <text class="block-label" x="510" y="418">Relationship</text>
    <text class="block-label" x="510" y="447">Management</text>
  </g>
  <g class="block teal">
    <polygon class="top face-edge" points="641,354 673,324 833,324 801,354"/>
    <polygon class="side" points="801,354 833,324 833,432 801,462"/>
    <rect class="front" x="641" y="354" width="160" height="108"/>
    <rect x="641" y="354" width="160" height="108" fill="url(#front-sheen)"/>
    <text class="block-label" x="721" y="389">Market &amp;</text>
    <text class="block-label" x="721" y="418">Communicate</text>
    <text class="block-label" x="721" y="447">Value</text>
  </g>

  <!-- Row 3 -->
  <g class="block red">
    <polygon class="top face-edge" points="339,236 371,206 531,206 499,236"/>
    <polygon class="side" points="499,236 531,206 531,313 499,343"/>
    <rect class="front" x="339" y="236" width="160" height="107"/>
    <rect x="339" y="236" width="160" height="107" fill="url(#front-sheen)"/>
    <text class="block-label" x="419" y="271">Maintain IT</text>
    <text class="block-label" x="419" y="300">Operational</text>
    <text class="block-label" x="419" y="329">Excellence</text>
  </g>
  <g class="block orange">
    <polygon class="top face-edge" points="558,231 590,201 750,201 718,231"/>
    <polygon class="side" points="718,231 750,201 750,308 718,338"/>
    <rect class="front" x="558" y="231" width="160" height="107"/>
    <rect x="558" y="231" width="160" height="107" fill="url(#front-sheen)"/>
    <text class="block-label" x="638" y="266">Create</text>
    <text class="block-label" x="638" y="295">Business</text>
    <text class="block-label" x="638" y="324">Value</text>
  </g>

  <!-- Apex -->
  <g class="block green">
    <polygon class="top face-edge" points="458,118 490,88 650,88 618,118"/>
    <polygon class="side" points="618,118 650,88 650,195 618,225"/>
    <rect class="front" x="458" y="118" width="160" height="107"/>
    <rect x="458" y="118" width="160" height="107" fill="url(#front-sheen)"/>
    <text class="block-label block-label--apex" x="538" y="166">IT VISION &amp;</text>
    <text class="block-label block-label--apex" x="538" y="195">LEADERSHIP</text>
  </g>
</svg>
</body>
</html>
```